Mossy Den Pet Supply

Thank you for your interest in this design contest. We are always welcome to questions and are looking forward to seeing what you can come up with.

We work on a Bootstrap platform with our custom built CMS. We require all designs to be sized accordingly with the bootstrap grid system found here: http://fernlattice.com/css/#grid

At the start of a competition, we are looking for general Home Page Design concepts and an example product grid page.

Homepage: Slide Show/Featured Products/Specials

example website as a reference:https://www.mintcollarworks.com/

Store Product Grid: Show a grid of product thumbnails. Included elements are thumbnail and price. Also included are filters (sort by, show by grid/list).

No photos at this time but Logo is attached. Looking for good quality photo's around the web. Please read the attached creative brief in depth to get an idea f what the client is looking for. Thanks!

```html
<!DOCTYPE html>
<html lang="en">
<head>
<meta charset="utf-8">
<title>Mossy Den Pet Supply</title>
<link rel="stylesheet" href="https://fonts.googleapis.com/css2?family=Figtree:wght@400;600;700&display=swap">
<style>
:root{
  --green:#92c83e;
  --green-dark:#7eb42f;
  --green-deep:#6da02a;
  --gold:#d8a44d;
  --yellow:#f2c955;
  --mint:#eef5e7;
  --text:#5a5a5a;
  --muted:#9a9a9a;
  --heading:#5b7a3c;
  --white:#fff;
}
*{box-sizing:border-box;margin:0;padding:0}
html,body{width:933px;height:1200px;overflow:hidden}
body{position:relative;font-family:"Figtree",sans-serif;color:var(--text);background:var(--white)}
.abs{position:absolute}
.topbar{left:0;top:0;width:933px;height:23px;background:var(--green-dark);font-size:8px;color:var(--white);font-weight:600}
.topbar span{position:absolute;top:7px;display:flex;align-items:center;gap:6px}
.navbar{left:0;top:23px;width:933px;height:78px;background:var(--green)}
.logo-box{left:114px;top:0;width:108px;height:106px;background:var(--white);box-shadow:0 1px 3px rgba(0,0,0,.15);display:flex;flex-direction:column;align-items:center;justify-content:center;gap:6px;z-index:3;text-align:center}
.logo-dot{width:30px;height:30px;background:#222;border-radius:50%}
.logo-name{font-size:11px;font-weight:700;color:#222;line-height:1.15}
.nav{left:288px;top:23px;display:flex;height:78px}
.nav a{width:93px;display:flex;align-items:center;justify-content:center;color:var(--white);font-size:10px;font-weight:700;text-decoration:none;border-left:1px solid rgba(255,255,255,.2)}
.nav a:last-child{border-right:1px solid rgba(255,255,255,.2)}
.nav a.active{background:var(--green-deep)}
.cart{left:771px;top:43px;width:46px;height:46px;border-radius:50%;background:var(--gold);display:flex;align-items:center;justify-content:center;box-shadow:0 0 0 4px rgba(216,164,77,.25)}
.hero{left:0;top:101px;width:933px;height:346px;background:linear-gradient(100deg,#dcd6d0 0%,#ece8e4 45%,#d4cbc2 70%,#b9a08a 100%)}
.hero-title{left:162px;top:212px;font-size:38px;font-weight:700;color:var(--white);text-shadow:0 1px 3px rgba(0,0,0,.3)}
.hero-text{left:162px;top:266px;font-size:16px;line-height:22px;color:var(--white);text-shadow:0 1px 2px rgba(0,0,0,.3)}
.btn{display:flex;align-items:center;justify-content:center;color:var(--white);font-size:10px;font-weight:700}
.hero-btn{left:164px;top:326px;width:109px;height:29px;background:var(--gold)}
.arrow{width:48px;height:48px;border-radius:50%;display:flex;align-items:center;justify-content:center}
.arrow-prev{left:45px;top:249px;background:var(--white)}
.arrow-next{left:840px;top:249px;background:var(--green)}
.section-title{left:0;width:933px;top:468px;text-align:center;font-size:16px;color:var(--heading)}
.card{top:502px;width:223px;height:211px}
.card-img{height:145px}
.card-info{height:66px;background:var(--mint);position:relative;padding:17px 0 0 20px}
.card-info .name{font-size:10px}
.card-info .price{font-size:13px;color:var(--green);margin-top:5px}
.card.on .card-info{background:var(--green)}
.card.on .name,.card.on .price{color:var(--white)}
.basket{position:absolute;right:15px;top:15px;width:34px;height:34px;border-radius:50%;background:var(--green);display:flex;align-items:center;justify-content:center}
.card.on .basket{background:var(--white)}
.specials{left:112px;top:731px;width:467px;height:223px;background:#f6f3ec}
.spec-tab{left:0;top:0;width:125px;height:223px;background:var(--yellow);display:flex;align-items:center;justify-content:center;color:var(--white);font-size:16px}
.spec-img{left:125px;top:40px;width:342px;height:183px;background:radial-gradient(ellipse at 45% 55%,#ead8b6 0%,#d8bd93 45%,#f6f3ec 80%)}
.spec-name{right:22px;top:34px;font-size:12px;text-align:right}
.spec-price{right:22px;top:51px;font-size:18px;color:var(--green)}
.spec-btn{left:336px;top:79px;width:110px;height:28px;background:var(--green)}
.news{left:601px;top:731px;width:222px;height:223px;background:var(--mint)}
.news h3{position:absolute;left:0;width:222px;top:20px;text-align:center;font-size:17px;font-weight:400;color:var(--heading)}
.field{left:21px;width:187px;height:38px;background:var(--white);border:1px solid #dfe6d8;font-size:9px;color:var(--muted);padding:13px 12px}
.field b{color:#e05a4a;font-weight:400}
.tick{left:25px;top:167px;width:18px;height:18px;background:var(--green);display:flex;align-items:center;justify-content:center}
.news-note{left:52px;top:165px;font-size:9.5px;line-height:15px;color:#666}
.divider{left:0;top:974px;width:933px;height:1px;background:#e8e8e8}
.foot-logo{left:114px;top:1005px;width:110px;height:127px;display:flex;flex-direction:column;align-items:center;justify-content:center;gap:8px;text-align:center}
.foot-logo .logo-dot{width:40px;height:40px}
.foot-logo .logo-name{font-size:13px}
.foot-h{font-size:12px;font-weight:600;color:var(--heading);letter-spacing:.5px}
.foot-links{font-size:8.5px;color:var(--muted);line-height:23px}
.foot-links li{list-style:none}
.foot-links li::before{content:"›";margin-right:5px}
.contact{font-size:9px;color:var(--muted);line-height:21px}
.contact a{color:var(--green);text-decoration:none}
.social{top:1026px;width:24px;height:24px}
.badge{top:1111px;width:39px;height:25px;border:1px solid #e1e1e1;display:flex;align-items:center;justify-content:center;font-size:7px;font-weight:600;color:#555}
.bottombar{left:0;top:1156px;width:933px;height:44px;background:var(--green);font-size:9.5px;color:var(--heading)}
</style>
</head>
<body>
<div class="abs topbar">
  <span style="left:610px"><svg width="13" height="9" viewBox="0 0 13 9"><rect x="0.5" y="0.5" width="12" height="8" fill="none" stroke="#fff"/><path d="M1 1l5.5 4L12 1" fill="none" stroke="#fff"/></svg>hello@mossyden.com</span>
  <span style="left:734px"><svg width="10" height="10" viewBox="0 0 10 10"><path d="M2 1l2 2-1 1.5c.7 1.3 1.6 2.2 2.5 2.5L7 6l2 2-1.5 1.5C4 9 1 6 .5 2.5z" fill="#fff"/></svg>+84 555 010 477</span>
</div>
<div class="abs navbar"></div>
<div class="abs logo-box"><div class="logo-dot"></div><div class="logo-name">MOSSY DEN<br>PET SUPPLY</div></div>
<nav class="abs nav">
  <a class="active">HOME</a><a>PRODUCTS</a><a>SPECIALS</a><a>ABOUT</a><a>CONTACT</a>
</nav>
<div class="abs cart"><svg width="18" height="16" viewBox="0 0 18 16"><path d="M1 1h3l2 9h9l2-6H5" fill="none" stroke="#fff" stroke-width="2"/><circle cx="7" cy="13.5" r="1.6" fill="#fff"/><circle cx="14" cy="13.5" r="1.6" fill="#fff"/></svg></div>

<div class="abs hero" role="img" aria-label="Photo of a small white and brown dog sleeping on a soft knitted bed">
  <div class="abs hero-title" style="top:111px">Dog Beds</div>
  <div class="abs hero-text" style="top:165px">Lorem ipsum dolor sit amet, consec-<br>tetuer adipiscing elit</div>
  <div class="abs btn hero-btn" style="top:225px">BUY NOW</div>
  <div class="abs arrow arrow-prev" style="top:148px"><svg width="14" height="22" viewBox="0 0 14 22"><path d="M11 2L3 11l8 9" fill="none" stroke="#bbb" stroke-width="2.5"/></svg></div>
  <div class="abs arrow arrow-next" style="top:148px"><svg width="14" height="22" viewBox="0 0 14 22"><path d="M3 2l8 9-8 9" fill="none" stroke="#fff" stroke-width="2.5"/></svg></div>
</div>

<h2 class="abs section-title" style="font-weight:400">Featured Products</h2>

<div class="abs card" style="left:111px">
  <div class="card-img" role="img" aria-label="Photo of a small terrier wearing a collar" style="background:linear-gradient(120deg,#e8c39a,#c98a55 60%,#7a4a2a)"></div>
  <div class="card-info"><div class="name">Cute Dog Collar</div><div class="price">$300</div>
    <div class="basket"><svg width="16" height="14" viewBox="0 0 16 14"><path d="M1 5h14l-2 8H3z" fill="#fff"/><path d="M4 5l4-4 4 4" fill="none" stroke="#fff" stroke-width="1.5"/></svg></div></div>
</div>
<div class="abs card on" style="left:357px">
  <div class="card-img" role="img" aria-label="Photo of a golden retriever lying on a green dog bed" style="background:linear-gradient(180deg,#8aa53a 0%,#6f8f2e 40%,#2e4a2a 70%,#1f3a22 100%)"></div>
  <div class="card-info"><div class="name">Fluffy Dog Bed</div><div class="price">$300</div>
    <div class="basket"><svg width="16" height="14" viewBox="0 0 16 14"><path d="M1 5h14l-2 8H3z" fill="#92c83e"/><path d="M4 5l4-4 4 4" fill="none" stroke="#92c83e" stroke-width="1.5"/></svg></div></div>
</div>
<div class="abs card" style="left:601px">
  <div class="card-img" role="img" aria-label="Photo of a cream puppy chewing a red leash" style="background:linear-gradient(120deg,#c9cdb0,#ece6d6 50%,#b9bca3)"></div>
  <div class="card-info"><div class="name">Red Dog Leashes</div><div class="price">$300</div>
    <div class="basket"><svg width="16" height="14" viewBox="0 0 16 14"><path d="M1 5h14l-2 8H3z" fill="#fff"/><path d="M4 5l4-4 4 4" fill="none" stroke="#fff" stroke-width="1.5"/></svg></div></div>
</div>

<div class="abs specials">
  <div class="abs spec-img" role="img" aria-label="Photo of a yellow labrador lying on a patterned dog bed"></div>
  <div class="abs spec-tab">SPECIALS</div>
  <svg class="abs" style="left:124px;top:104px" width="7" height="14" viewBox="0 0 7 14"><path d="M0 0l7 7-7 7z" fill="#f2c955"/></svg>
  <div class="abs spec-name">Royal Dog Bed</div>
  <div class="abs spec-price">$300</div>
  <div class="abs btn spec-btn">BUY NOW</div>
</div>

<div class="abs news">
  <h3>Signup for our Newletter</h3>
  <div class="abs field" style="top:52px">Enter Name</div>
  <div class="abs field" style="top:99px">Enter Your Email <b>*</b></div>
  <div class="abs tick"><svg width="10" height="8" viewBox="0 0 10 8"><path d="M1 4l3 3 5-6" fill="none" stroke="#fff" stroke-width="1.6"/></svg></div>
  <div class="abs news-note">Send me Newsletters, promise<br>we're not gonna spam you.</div>
</div>

<div class="abs divider"></div>

<div class="abs foot-logo"><div class="logo-dot"></div><div class="logo-name">MOSSY DEN<br>PET SUPPLY</div></div>

<div class="abs foot-h" style="left:309px;top:996px">NAVIGATION</div>
<ul class="abs foot-links" style="left:312px;top:1019px"><li>Home</li><li>Products</li><li>Specials</li><li>About</li><li>Contact</li></ul>
<ul class="abs foot-links" style="left:383px;top:1019px"><li>Login</li><li>Register</li><li>My Cart</li><li>Checkout</li><li>FAQ</li></ul>

<div class="abs foot-h" style="left:478px;top:996px">CONTACT INFO</div>
<div class="abs contact" style="left:478px;top:1022px">MOSSY DEN, Company Inc.<br>4410 Fernbrook Street<br>Your Country, USA</div>
<div class="abs contact" style="left:478px;top:1099px">Phone: (+99) 555 014 2290<br>E-mail: <a>info@mossyden.com</a></div>

<div class="abs foot-h" style="left:674px;top:996px">GET SOCIAL</div>
<div class="abs social" style="left:676px;background:#3b5998" role="img" aria-label="Facets"></div>
<div class="abs social" style="left:711px;background:#2aa3ef" role="img" aria-label="Chatter"></div>
<div class="abs social" style="left:746px;background:#0e76a8" role="img" aria-label="Linkup"></div>

<div class="abs foot-h" style="left:674px;top:1088px">WE ACCEPT</div>
<div class="abs badge" style="left:674px;background:#fdf4e0">PayWell</div>
<div class="abs badge" style="left:728px;background:#f3f3f3">CardOne</div>
<div class="abs badge" style="left:780px;background:#1d3f8e;color:#fff;border-color:#1d3f8e">Mercato</div>

<div class="abs bottombar">
  <span class="abs" style="left:114px;top:16px">Copyright © 2014 - MOSSY DEN PET SUPPLY</span>
  <span class="abs" style="right:143px;top:16px">Sitemap &nbsp; | &nbsp; Privacy Policy</span>
</div>
</body>
</html>
```